Corvale Real Estate

I manage 2 firms. The first one is Pelmora and the logo is in blue (see the file) but i need a design for my business card for the second firm called CORVALE IMMOBILIER. This one is in charge of Real estate developer.

Colors
3176b5

```html
<!DOCTYPE html>
<html lang="fr">
<head>
<meta charset="utf-8">
<title>Corvale Immobilier — Business Card</title>
<link rel="stylesheet" href="https://fonts.googleapis.com/css2?family=Montserrat:wght@500;600&family=Source+Sans+3:wght@400;600;700&display=swap">
<style>
  :root {
    --brand-blue: #3959a8;
    --brand-grey: #9a9a9c;
    --band-grey: #b9babd;
    --ink: #1e1e22;
    --paper: #ffffff;
    --backdrop: #e4e5e7;
  }
  * { box-sizing: border-box; margin: 0; padding: 0; }
  html, body {
    width: 1200px; height: 800px; overflow: hidden;
    background: var(--backdrop);
  }
  .canvas {
    position: relative; width: 1200px; height: 800px;
    display: flex; flex-direction: column; align-items: center; justify-content: center; gap: 44px;
  }
  .card {
    position: relative; width: 560px; height: 320px; overflow: hidden;
    box-shadow: 0 6px 18px rgba(0,0,0,.18);
  }

  /* Front side */
  .card--front { background: var(--brand-blue); }
  .front-brand { position: absolute; left: 44px; top: 150px; }
  .wordmark {
    font-family: "Montserrat", sans-serif; font-weight: 600;
    font-size: 46px; line-height: 1; letter-spacing: 1px; color: var(--paper);
  }
  .wordmark-sub {
    font-family: "Montserrat", sans-serif; font-weight: 500;
    font-size: 14px; letter-spacing: 11px; color: var(--band-grey);
    margin-top: 2px; padding-left: 4px;
  }
  .front-web {
    margin-top: 10px;
    font-family: "Source Sans 3", sans-serif; font-size: 15px; color: var(--paper);
  }
  .front-web b { font-weight: 700; }

  /* Back side */
  .card--back { background: var(--paper); }
  .back-brand {
    position: absolute; left: 40px; top: 36px;
    display: flex; align-items: center; gap: 16px;
  }
  .brand-square { width: 34px; height: 34px; background: var(--brand-blue); }
  .brand-divider { width: 1px; height: 48px; background: var(--band-grey); }
  .back-brand .wordmark { font-size: 36px; color: var(--brand-blue); }
  .back-brand .wordmark-sub { font-size: 11px; letter-spacing: 9px; color: var(--brand-grey); }

  .contact {
    position: absolute; left: 40px; top: 168px; list-style: none;
    font-family: "Source Sans 3", sans-serif; font-size: 15px; line-height: 1.25; color: var(--ink);
  }
  .contact li { display: flex; align-items: flex-start; gap: 7px; margin-bottom: 3px; }
  .contact svg { flex: none; margin-top: 2px; fill: var(--brand-blue); }

  .holder { position: absolute; right: 56px; top: 160px; text-align: left; }
  .holder-name {
    font-family: "Source Sans 3", sans-serif; font-weight: 700; font-size: 21px; color: var(--brand-blue);
  }
  .holder-role {
    font-family: "Source Sans 3", sans-serif; font-size: 16px; color: var(--ink); padding-left: 22px;
  }

  .footer-bands { position: absolute; left: 0; bottom: 0; width: 560px; height: 80px; }
  .footer-web {
    position: absolute; right: 40px; bottom: 14px;
    font-family: "Source Sans 3", sans-serif; font-size: 17px; color: var(--paper);
  }
  .footer-web b { font-weight: 700; }
</style>
</head>
<body>
<main class="canvas">

  <section class="card card--front" aria-label="Recto">
    <div class="front-brand">
      <div class="wordmark">CORVALE</div>
      <div class="wordmark-sub">IMMOBILIER</div>
      <div class="front-web">www.<b>corvaleimmobilier</b>.fr</div>
    </div>
  </section>

  <section class="card card--back" aria-label="Verso">
    <div class="back-brand">
      <span class="brand-square"></span>
      <span class="brand-divider"></span>
      <div>
        <div class="wordmark">CORVALE</div>
        <div class="wordmark-sub">IMMOBILIER</div>
      </div>
    </div>

    <ul class="contact">
      <li>
        <svg width="12" height="14" viewBox="0 0 12 16" aria-hidden="true"><path d="M6 0a6 6 0 0 0-6 6c0 4.5 6 10 6 10s6-5.5 6-10a6 6 0 0 0-6-6zm0 8.5A2.5 2.5 0 1 1 6 3.5a2.5 2.5 0 0 1 0 5z"/></svg>
        <span>27 Rue des Tilleuls<br>75016 Paris</span>
      </li>
      <li>
        <svg width="12" height="14" viewBox="0 0 16 16" aria-hidden="true"><path d="M3.6 1 6 3.6 4.6 5.6c.9 2 2.8 3.9 4.8 4.8l2-1.4L14 11.4 12.6 14C6.8 14 2 9.2 2 3.4z"/></svg>
        <span>041 582 3706</span>
      </li>
      <li>
        <svg width="14" height="12" viewBox="0 0 16 12" aria-hidden="true"><path d="M0 0h16v12H0zm1.5 1.5v.4L8 6.6l6.5-4.7v-.4zm0 2.2v6.8h13V3.7L8 8.4z"/></svg>
        <span>julien@corvaleimmobilier.fr</span>
      </li>
    </ul>

    <div class="holder">
      <div class="holder-name">Julien Marceau</div>
      <div class="holder-role">Managing Director</div>
    </div>

    <svg class="footer-bands" viewBox="0 0 560 80" aria-hidden="true">
      <polygon points="0,22 560,22 560,30 0,30" fill="var(--band-grey)"/>
      <polygon points="0,34 560,34 560,80 0,80" fill="var(--brand-blue)"/>
      <polygon points="0,34 200,34 200,46 0,46" fill="var(--band-grey)"/>
      <polygon points="200,34 214,46 200,46" fill="var(--band-grey)"/>
    </svg>
    <div class="footer-web">www.<b>corvaleimmobilier</b>.fr</div>
  </section>

</main>
</body>
</html>
```